Poster to advertise new mind coaching clinic

Create a single sided A4 colour poster using the text provided. Suggested image provided. You may want to suggest an alternative however images need to appeal to both male and female sports people.

Text:
One-to-one mind coaching
For recreational and competitive sports people
Learn the mental tools and techniques used by the top sports people to fulfil your potential

 Create well-formed and achievable goals
 Overcome limiting beliefs
 Accelerate mastery through modelling your heroes
 Learn how to use mental rehearsal to increase your chances of success
 Smash through belief ceilings
 Get into the zone to bring your ‘A-Game’ more often
Thursdays in central Twyford
5-8pm
For more information contact:
thebluekitecoaching@postmere.com
Tel: 07481 265314
www.the-blue-kite.co.uk

Target Market(s)

sports people

Industry/Entity Type

Clinic

Requirements
Must have
• All the content provided. Contact details.

```html
<!DOCTYPE html>
<html lang="en">
<head>
<meta charset="utf-8">
<title>The Blue Kite – One-to-one mind coaching</title>
<link href="https://fonts.googleapis.com/css2?family=PT+Sans+Narrow:wght@400;700&display=swap" rel="stylesheet">
<style>
  :root {
    --page-bg: #b9b9b9;
    --ink-top: #111111;
    --ink-black: #000000;
    --cyan: #3ec6ec;
    --white: #ffffff;
    --footer-ink: #111111;
    --purple: #5b3f9e;
    --magenta: #b2397a;
    --pink: #e21f68;
    --navy: #141640;
    --glow: #3552b8;
    --rule-yellow: #d9e021;
    --rule-teal: #1f8f82;
  }
  * { margin: 0; padding: 0; box-sizing: border-box; }
  html, body {
    width: 1200px; height: 1200px; overflow: hidden;
    background: var(--page-bg);
    font-family: "PT Sans Narrow", "Arial Narrow", sans-serif;
  }
  .poster {
    position: absolute; left: 186px; top: 22px;
    width: 1010px; height: 1410px;
    transform: scale(0.82); transform-origin: top left;
    overflow: hidden; background: var(--ink-black);
  }
  .poster-shapes { position: absolute; inset: 0; width: 1010px; height: 1410px; }
  .headline {
    position: absolute; white-space: nowrap; color: var(--white);
    line-height: 1;
  }
  .headline .accent { color: var(--cyan); font-weight: 700; }
  .headline .cyan { color: var(--cyan); }
  .headline-one { right: 318px; top: 92px; font-size: 37px; }
  .headline-one .accent { font-size: 46px; }
  .headline-two { right: 275px; top: 196px; font-size: 38px; }
  .headline-two .accent { font-size: 47px; }
  .headline-two .small { font-size: 34px; }
  .headline-three { right: 366px; top: 306px; color: var(--cyan); font-weight: 700; font-size: 40px; }
  .headline-three .big { font-size: 54px; }
  .headline-sub { left: 45px; top: 366px; font-size: 30px; }
  .benefits {
    position: absolute; left: 0; right: 0; top: 544px;
    list-style: none; text-align: center; color: var(--white);
    font-weight: 700; font-size: 34px; line-height: 47.6px;
  }
  .benefits li::before { content: "\2713"; margin-right: 8px; font-weight: 400; }
  .session-details, .contact-details {
    position: absolute; top: 1018px; width: 460px; text-align: center;
    color: var(--white); font-weight: 700;
  }
  .session-details { left: 27px; font-size: 36px; line-height: 52px; }
  .contact-details { left: 527px; font-size: 30px; line-height: 44px; }
  .contact-details .contact-lead { font-size: 32px; }
  .info-divider {
    position: absolute; left: 508px; top: 1013px; width: 2px; height: 142px;
    background: var(--white);
  }
  .brand-name {
    position: absolute; left: 62px; top: 1282px;
    display: flex; align-items: center; gap: 16px;
    color: var(--footer-ink); font-weight: 700; font-size: 56px;
  }
  .brand-mark { width: 40px; height: 40px; border-radius: 50%; background: var(--cyan); }
  .website {
    position: absolute; right: 43px; top: 1306px;
    color: var(--footer-ink); font-weight: 700; font-size: 36px;
  }
</style>
</head>
<body>
  <div class="poster">
    <svg class="poster-shapes" viewBox="0 0 1010 1410">
      <defs>
        <linearGradient id="bandGradient" x1="1" y1="0" x2="0.35" y2="1">
          <stop offset="0" stop-color="var(--purple)"/>
          <stop offset="0.5" stop-color="var(--magenta)"/>
          <stop offset="1" stop-color="var(--pink)"/>
        </linearGradient>
        <radialGradient id="bottomGlow" cx="0.5" cy="1" r="0.6">
          <stop offset="0" stop-color="var(--glow)"/>
          <stop offset="0.5" stop-color="var(--navy)"/>
          <stop offset="1" stop-color="#000"/>
        </radialGradient>
        <linearGradient id="ruleGradient" x1="0" y1="0" x2="1" y2="0">
          <stop offset="0" stop-color="var(--rule-yellow)"/>
          <stop offset="1" stop-color="var(--rule-teal)"/>
        </linearGradient>
        <linearGradient id="footerGradient" x1="0" y1="0" x2="1" y2="0">
          <stop offset="0" stop-color="#ffffff"/>
          <stop offset="1" stop-color="#dcdcdc"/>
        </linearGradient>
        <linearGradient id="runnerGradient" x1="0" y1="0" x2="1" y2="1">
          <stop offset="0" stop-color="#5c6670"/>
          <stop offset="1" stop-color="#1d2228"/>
        </linearGradient>
      </defs>
      <rect class="top-panel" x="0" y="0" width="1010" height="700" fill="var(--ink-top)"/>
      <rect class="bottom-panel" x="0" y="700" width="1010" height="545" fill="url(#bottomGlow)"/>
      <path class="colour-band" d="M0 490 C 320 545, 820 560, 1010 0 L1010 795 Q 560 1027 0 780 Z" fill="url(#bandGradient)"/>
      <path d="M0 490 C 320 545, 820 560, 1010 0" fill="none" stroke="#8a8a8a" stroke-width="4"/>
      <path d="M0 780 Q 560 1027 1010 795" fill="none" stroke="#9a9a9a" stroke-width="5"/>
      <rect class="headline-rule" x="0" y="139" width="700" height="6" fill="url(#ruleGradient)"/>
      <rect class="headline-rule" x="0" y="248" width="720" height="6" fill="url(#ruleGradient)"/>
      <rect class="headline-rule" x="0" y="407" width="590" height="6" fill="url(#ruleGradient)"/>
      <rect class="runner-photo" role="img" aria-label="Photo of a female athlete sprinting mid-stride" x="750" y="95" width="212" height="405" rx="90" fill="url(#runnerGradient)"/>
      <rect class="footer" x="0" y="1245" width="1010" height="165" fill="url(#footerGradient)"/>
    </svg>

    <p class="headline headline-one"><span class="accent">One-to-one</span> <span class="cyan">mind coaching</span></p>
    <p class="headline headline-two"><span class="accent">For</span> recreational <span class="small">and</span> competitive <span class="cyan">sports people</span></p>
    <p class="headline headline-three"><span class="big">Learn</span> the mental tools and techniques</p>
    <p class="headline headline-sub">used by the top sports people to fulfil your potential</p>

    <ul class="benefits">
      <li>Create well-formed and achievable goals</li>
      <li>Overcome limiting beliefs</li>
      <li>Accelerate mastery through modelling your heroes</li>
      <li>Learn how to use mental rehearsal to increase your chances of success</li>
      <li>Smash through belief ceilings</li>
      <li>Get into the zone to bring your ‘A-Game’ more often</li>
    </ul>

    <div class="session-details">
      <p>Thursdays in central Twyford</p>
      <p>5-8pm</p>
    </div>
    <div class="info-divider"></div>
    <div class="contact-details">
      <p class="contact-lead">For more information contact:</p>
      <p>thebluekitecoaching@postmere.com</p>
      <p>Tel: 07481 265314</p>
    </div>

    <div class="brand-name"><span class="brand-mark"></span><span>The Blue Kite</span></div>
    <p class="website">www.the-blue-kite.co.uk</p>
  </div>
</body>
</html>
```